I am a new company with the latest technology in the concrete polishing business

We need a logo design for a new company out of Toronto, Canada. We polish residential, commercial and industrial concrete as well as different epoxy toppings.

Target Market(s)

How Owners with expendable incomes

Industry/Entity Type

Construction

Contact Information for Business Card

be able to see content rather easily

Colors
0355a3
fbed22
1b1b1b

Requirements
Must have
• simple and elegant

```html
<!DOCTYPE html>
<html lang="en">
<head>
<meta charset="utf-8">
<title>Slabline Polish – Business Card</title>
<link href="https://fonts.googleapis.com/css2?family=Questrial&display=swap" rel="stylesheet">
<style>
  :root {
    --page-bg: #e6e6e6;
    --card-white: #ffffff;
    --card-black: #141414;
    --ink-dark: #1b1b1b;
    --accent-orange: #f26a1b;
    --accent-yellow: #fbed22;
    --name-gold: #f7b815;
    --text-light: #ffffff;
    --text-muted: #d4d4d4;
  }
  * { margin: 0; padding: 0; box-sizing: border-box; }
  html, body {
    width: 1200px; height: 900px; overflow: hidden;
    background: var(--page-bg);
    font-family: "Questrial", "Century Gothic", sans-serif;
  }
  .business-card {
    position: absolute;
    left: 100px; top: 165px;
    width: 1000px; height: 570px;
    border-radius: 36px;
    overflow: hidden;
    background: var(--card-white);
  }
  .card-shapes { position: absolute; inset: 0; }
  .brand {
    position: absolute;
    left: 40px; top: 0; width: 480px; height: 570px;
    display: flex; align-items: center; justify-content: center; gap: 18px;
  }
  .brand-dot {
    width: 34px; height: 34px; border-radius: 50%;
    background: var(--accent-orange);
    flex: none;
  }
  .brand-name {
    font-size: 46px;
    color: var(--ink-dark);
    letter-spacing: 1px;
    white-space: nowrap;
  }
  .contact {
    position: absolute;
    left: 610px; top: 0; width: 380px; height: 570px;
    display: flex; flex-direction: column; align-items: center; justify-content: center;
    text-align: center;
    color: var(--text-light);
  }
  .contact-name { font-size: 30px; color: var(--name-gold); }
  .contact-role { font-size: 19px; color: var(--text-muted); margin-top: 4px; }
  .contact-phone { font-size: 27px; margin-top: 80px; }
  .contact-line { font-size: 21px; line-height: 1.4; }
  .contact-links { margin-top: 14px; }
  .contact-address { margin-top: 20px; }
</style>
</head>
<body>
  <div class="business-card">
    <svg class="card-shapes" viewBox="0 0 1000 570" width="1000" height="570" aria-hidden="true">
      <defs>
        <linearGradient id="accentBand" x1="0" y1="0" x2="0" y2="1">
          <stop offset="0" stop-color="var(--accent-orange)"/>
          <stop offset="0.55" stop-color="var(--accent-yellow)"/>
          <stop offset="1" stop-color="var(--accent-orange)"/>
        </linearGradient>
      </defs>
      <path class="accent-band" d="M470 0 C600 140 610 380 500 570 L1000 570 L1000 0 Z" fill="url(#accentBand)"/>
      <path class="dark-panel" d="M640 0 C610 250 570 420 480 570 L1000 570 L1000 0 Z"
            fill="var(--card-black)" stroke="var(--card-white)" stroke-width="6"/>
    </svg>

    <div class="brand">
      <span class="brand-dot"></span>
      <span class="brand-name">Slabline Polish</span>
    </div>

    <div class="contact">
      <p class="contact-name">Marcus Delane</p>
      <p class="contact-role">Owner</p>
      <p class="contact-phone">(555) 014-2290</p>
      <div class="contact-links">
        <p class="contact-line">info@slablinepolish.com</p>
        <p class="contact-line">www.slablinepolish.com</p>
      </div>
      <div class="contact-address">
        <p class="contact-line">4820 Ridgeway Road,</p>
        <p class="contact-line">Austin, Texas 78701</p>
      </div>
    </div>
  </div>
</body>
</html>
```